Financial Services Sales Sheet

We need this sheet redesigned. Needs to feel very corporate/financial. open to imagery/icons/colors/etc. Copy is in the docx file to expedite work. PDF is what client has done inh-house and feels dated.

```html
<!DOCTYPE html>
<html lang="en">
<head>
<meta charset="utf-8">
<title>Harborline Capital Partners — Master Servicing &amp; Portfolio Optimization</title>
<link href="https://fonts.googleapis.com/css2?family=Montserrat:wght@600;700;800&family=Inter:wght@400;500;600&display=swap" rel="stylesheet">
<style>
  :root{
    --page-bg:#e6e9ed;
    --navy:#13294b;
    --navy-deep:#0c1d38;
    --accent:#2c6db5;
    --white:#ffffff;
    --ink:#1b2233;
    --muted:#48536a;
    --silver-top:#fbfbfc;
    --silver-bottom:#d5d9df;
    --hero-photo-a:#7f93ab;
    --hero-photo-b:#cfd8e2;
  }
  *{box-sizing:border-box;margin:0;padding:0}
  html,body{width:1200px;height:1200px;overflow:hidden}
  body{background:var(--page-bg);font-family:"Inter",Arial,sans-serif;color:var(--ink);position:relative}

  .sheet{position:absolute;left:210px;top:40px;width:780px;height:1120px;background:var(--white);overflow:hidden;box-shadow:0 6px 24px rgba(12,29,56,.18)}

  .hero-photo{position:absolute;right:0;top:0;width:460px;height:425px;background:linear-gradient(160deg,var(--hero-photo-b) 0%,var(--hero-photo-a) 55%,#40597a 100%)}
  .hero-band{position:absolute;left:0;top:100px;width:780px;height:325px;background:linear-gradient(90deg,var(--navy) 0%,var(--navy) 50%,rgba(19,41,75,.55) 78%,rgba(19,41,75,.15) 100%)}
  .header-fade{position:absolute;left:0;top:0;width:780px;height:100px;background:linear-gradient(90deg,var(--white) 0%,var(--white) 48%,rgba(255,255,255,.35) 70%,rgba(255,255,255,0) 100%)}

  .brand{position:absolute;left:38px;top:30px;display:flex;align-items:center;gap:12px}
  .brand-square{width:34px;height:34px;background:var(--navy)}
  .brand-name{font-family:"Montserrat",Arial,sans-serif;font-weight:700;font-size:19px;line-height:1.15;color:var(--navy);text-transform:uppercase}

  .hero-title{position:absolute;left:38px;top:122px;width:560px;font-family:"Montserrat",Arial,sans-serif;font-weight:800;font-size:41px;line-height:1.1;color:var(--white)}
  .hero-subtitle{position:absolute;left:38px;top:228px;width:520px;font-family:"Inter",Arial,sans-serif;font-weight:500;font-size:21px;line-height:1.2;color:#dbe3ee}
  .hero-intro{position:absolute;left:38px;top:292px;width:470px;font-size:14.5px;line-height:1.3;color:#e8edf4}

  .service-cards{position:absolute;left:38px;top:363px;width:704px;display:flex;gap:18px}
  .service-card{flex:1;height:220px;background:linear-gradient(180deg,var(--silver-top),var(--silver-bottom));border:1px solid #c3c9d2;border-radius:6px;box-shadow:0 4px 10px rgba(12,29,56,.25);padding:18px 16px;text-align:center}
  .service-icon{width:60px;height:54px;display:block;margin:0 auto 10px}
  .service-title{font-family:"Inter",Arial,sans-serif;font-weight:600;font-size:18px;line-height:1.2;color:var(--navy-deep);margin-bottom:12px}
  .service-point{font-size:14.5px;line-height:1.25;color:var(--ink);text-align:left;padding-left:14px;position:relative}
  .service-point::before{content:"";position:absolute;left:2px;top:7px;width:5px;height:5px;border-radius:50%;background:var(--ink)}

  .snapshot-heading{position:absolute;left:38px;top:612px;font-family:"Inter",Arial,sans-serif;font-weight:600;font-size:27px;color:var(--navy-deep)}
  .stats{position:absolute;left:38px;top:652px;width:704px;height:115px;display:flex;gap:12px}
  .stat{background:linear-gradient(180deg,var(--silver-top),var(--silver-bottom));border:1px solid #c3c9d2;border-radius:5px;padding:10px 8px;text-align:center;display:flex;flex-direction:column;justify-content:center}
  .stat-1{flex:158}.stat-2{flex:191}.stat-3{flex:177}.stat-4{flex:158}
  .stat-value{font-family:"Inter",Arial,sans-serif;font-weight:600;font-size:31px;line-height:1.05;color:var(--navy-deep)}
  .stat-label{font-size:14.5px;line-height:1.2;color:var(--muted);margin-top:6px}

  .platform-band{position:absolute;left:0;top:790px;width:780px;height:315px;background:var(--navy)}
  .platform-photo{position:absolute;right:0;top:0;width:450px;height:315px;background:linear-gradient(150deg,#4d6788 0%,#2a4064 50%,#1b2d4c 100%)}
  .platform-fade{position:absolute;left:0;top:0;width:780px;height:315px;background:linear-gradient(90deg,var(--navy) 0%,var(--navy) 40%,rgba(19,41,75,.6) 55%,rgba(19,41,75,0) 72%)}
  .platform-name{position:absolute;left:38px;top:24px;font-family:"Inter",Arial,sans-serif;font-weight:600;font-size:28px;color:var(--white)}
  .platform-tagline{position:absolute;left:38px;top:70px;width:330px;font-weight:600;font-size:20px;line-height:1.2;color:var(--white)}
  .platform-copy{position:absolute;left:38px;top:140px;width:335px;font-size:14.5px;line-height:1.32;color:#dfe6ef}
  .accent-stripe{position:absolute;left:0;top:1105px;width:780px;height:15px;background:linear-gradient(90deg,var(--navy-deep),var(--accent))}
</style>
</head>
<body>
<main class="sheet">
  <div class="hero-photo" role="img" aria-label="Financial analytics dashboards and compliance charts on office monitors"></div>
  <div class="hero-band"></div>
  <div class="header-fade"></div>

  <header class="brand">
    <span class="brand-square"></span>
    <span class="brand-name">Harborline Capital<br>Partners</span>
  </header>

  <h1 class="hero-title">Master Servicing &amp; Portfolio Optimization</h1>
  <p class="hero-subtitle">End-to-End Post Default Management Strategy, Recovery &amp; Compliance</p>
  <p class="hero-intro">Harborline Capital Partners brings seasoned specialists, servicing metrics, portfolio analytics, compliance dashboards and investment-grade reporting to every engagement.</p>

  <section class="service-cards">
    <article class="service-card">
      <svg class="service-icon" viewBox="0 0 60 54" fill="none" stroke="#13294b" stroke-width="2.2" stroke-linecap="round" stroke-linejoin="round">
        <ellipse cx="14" cy="46" rx="9" ry="3"/><path d="M5 46v-5c0 1.7 4 3 9 3s9-1.3 9-3v5"/><ellipse cx="14" cy="41" rx="9" ry="3"/>
        <ellipse cx="34" cy="46" rx="9" ry="3"/><path d="M25 46V34"/><path d="M43 46V34"/><ellipse cx="34" cy="34" rx="9" ry="3"/><path d="M25 40c0 1.7 4 3 9 3s9-1.3 9-3"/>
        <path d="M10 30l12-10 8 6 20-20"/><path d="M42 6h8v8"/>
      </svg>
      <h2 class="service-title">Strategy &amp; Recovery Optimization</h2>
      <p class="service-point">Comprehensive recovery planning, data-driven optimization.</p>
    </article>
    <article class="service-card">
      <svg class="service-icon" viewBox="0 0 60 54" fill="none" stroke="#13294b" stroke-width="2.2" stroke-linecap="round" stroke-linejoin="round">
        <path d="M27 3l18 7v13c0 12-8 21-18 25C17 44 9 35 9 23V10z"/>
        <circle cx="40" cy="38" r="9" fill="#fff"/><path d="M36 38l3 3 5-6"/>
      </svg>
      <h2 class="service-title">Compliance &amp; Risk Oversight</h2>
      <p class="service-point">Regulatory compliance, continuous risk management.</p>
    </article>
    <article class="service-card">
      <svg class="service-icon" viewBox="0 0 60 54" fill="none" stroke="#13294b" stroke-width="2.2" stroke-linecap="round" stroke-linejoin="round">
        <circle cx="14" cy="22" r="5"/>
        <path d="M14 9v4M14 31v4M1 22h4M23 22h4M5 13l3 3M20 28l3 3M5 31l3-3M20 16l3-3"/>
        <rect x="29" y="8" width="11" height="38" rx="1"/><rect x="43" y="8" width="11" height="38" rx="1"/>
        <path d="M32 16h5M46 16h5"/><circle cx="34.5" cy="36" r="2"/><circle cx="48.5" cy="36" r="2"/>
      </svg>
      <h2 class="service-title">Operations &amp; Portfolio Management</h2>
      <p class="service-point">Efficient operational workflows, portfolio performance analysis.</p>
    </article>
  </section>

  <h2 class="snapshot-heading">Performance Snapshot</h2>
  <section class="stats">
    <div class="stat stat-1"><div class="stat-value">$155+<br>Million</div><div class="stat-label">Metrics</div></div>
    <div class="stat stat-2"><div class="stat-value">573,000+</div><div class="stat-label">Loans serviced to resolution</div></div>
    <div class="stat stat-3"><div class="stat-value">3,700+</div><div class="stat-label">Portfolios under management</div></div>
    <div class="stat stat-4"><div class="stat-value">21%</div><div class="stat-label">Average lift in recoveries</div></div>
  </section>

  <section class="platform-band">
    <div class="platform-photo" role="img" aria-label="Operations room with multi-monitor analytics workstation"></div>
    <div class="platform-fade"></div>
    <h2 class="platform-name">LedgerSight™</h2>
    <p class="platform-tagline">“The Intelligence Behind Every Compliant Command.”</p>
    <p class="platform-copy">A secure operations center with multi-monitor oversight, organized compliance data feeds, an AI-powered intelligence dashboard and real-time alerts, set against calm military blue hues.</p>
  </section>
  <div class="accent-stripe"></div>
</main>
</body>
</html>
```